Orbell Consulting- executive coaching business

looking for business card design for a newly started coaching business.
specialising in Exective coaching, Leadership, NLP and Motivation.
Looking for a simple, classy design using the existing logo attached and colour themes that complement the logo.
No red or orange in the business card design please.

Target Market(s)

Defence and Veteran community

Industry/Entity Type

Life Coaching

Contact Information for Business Card

looking for business cards for newly started coaching business.
specialising in Exective Coaching, Leadership, NLP and Motivation

Font styles to use
Serif
Script

Colors
0556a4
3176b5
86cfc6
33b8a4

Requirements
Must have
• Logo
• Email address- Jess@orbellconsulting.com.au
• Contact number
• Services provided - Executive Coaching, Leadership, NLP and Motivational Mapping.
Nice to have
• Same colours as logo
Should not have
• Red or orange

```html
<!DOCTYPE html>
<html lang="en">
<head>
<meta charset="utf-8">
<title>Orbell Consulting – Business Card</title>
<link rel="stylesheet" href="https://fonts.googleapis.com/css2?family=Raleway:wght@400;500;600&display=swap">
<style>
  :root {
    --page: #e9e7e3;
    --paper: #ffffff;
    --sky: #2aaee2;
    --sky-deep: #1f8fd6;
    --royal: #1c5cb3;
    --navy: #1844a3;
    --ink-blue: #1a56b0;
    --ring: #a9a9a9;
  }
  * { box-sizing: border-box; margin: 0; padding: 0; }
  html, body {
    width: 1200px; height: 821px; overflow: hidden;
    background: var(--page);
    font-family: "Raleway", sans-serif;
  }
  .sheet {
    width: 1200px; height: 821px;
    display: flex; align-items: center; justify-content: center; gap: 40px;
  }
  .card {
    width: 540px; height: 309px;
    background: var(--paper);
    box-shadow: 0 6px 18px rgba(0,0,0,.18);
    position: relative; overflow: hidden;
  }

  /* Back side */
  .card-back { display: flex; }
  .brand-panel {
    width: 233px; display: flex; flex-direction: column;
    align-items: center; justify-content: center; gap: 18px;
  }
  .brand-mark {
    width: 150px; height: 150px; border-radius: 50%;
    border: 3px solid var(--ring);
  }
  .brand-name {
    font-weight: 600; font-size: 18px; color: var(--ink-blue);
    letter-spacing: .2px; text-transform: uppercase;
  }
  .info-panel { flex: 1; display: flex; flex-direction: column; }
  .contact {
    height: 151px;
    background: linear-gradient(180deg, var(--sky) 0%, var(--sky-deep) 100%);
    display: flex; flex-direction: column; justify-content: center;
    gap: 12px; padding-left: 16px;
  }
  .contact-line {
    display: flex; align-items: center; gap: 11px;
    color: #fff; font-size: 17px; font-weight: 400;
  }
  .contact-icon { width: 23px; height: 23px; flex: none; }
  .services-title {
    color: var(--ink-blue); font-size: 22px; font-weight: 400;
    padding: 4px 0 0 34px; height: 34px; letter-spacing: .2px;
  }
  .service {
    height: 26px; display: flex; align-items: center;
    padding-left: 34px; font-size: 17px; font-weight: 400;
    color: var(--ink-blue);
  }
  .service.band { background: var(--royal); color: #fff; }
  .service.band-dark { background: var(--navy); color: #fff; }
  .footer-band { flex: 1; background: var(--navy); }

  /* Front side */
  .card-front {
    display: flex; flex-direction: column; align-items: center; justify-content: center; gap: 26px;
  }
  .front-mark {
    width: 110px; height: 110px; border-radius: 50%;
    border: 3px solid var(--ring);
  }
  .front-name {
    font-weight: 600; font-size: 36px; color: var(--ink-blue);
    text-transform: uppercase; letter-spacing: .5px;
  }
</style>
</head>
<body>
<main class="sheet">
  <section class="card card-back" aria-label="Card back">
    <div class="brand-panel">
      <div class="brand-mark"></div>
      <div class="brand-name">Orbell Consulting</div>
    </div>
    <div class="info-panel">
      <div class="contact">
        <div class="contact-line">
          <svg class="contact-icon" viewBox="0 0 24 24" aria-hidden="true">
            <circle cx="12" cy="12" r="12" fill="#fff"/>
            <rect x="6" y="8" width="12" height="8.5" rx="1" fill="#2aaee2"/>
            <path d="M6.5 8.5 L12 13 L17.5 8.5" fill="none" stroke="#fff" stroke-width="1.2"/>
          </svg>
          <span>Jess@orbellconsulting.com.au</span>
        </div>
        <div class="contact-line">
          <svg class="contact-icon" viewBox="0 0 24 24" aria-hidden="true">
            <circle cx="12" cy="12" r="12" fill="#fff"/>
            <path d="M8.6 6.5c.5-.3 1-.2 1.3.3l1 1.8c.3.5.2 1-.2 1.3l-.8.6c.5 1.4 1.5 2.5 2.9 3.1l.6-.8c.3-.4.9-.5 1.3-.2l1.8 1c.5.3.6.9.3 1.3l-.7 1c-.4.5-1.1.7-1.7.5-3.3-1-5.8-3.5-6.8-6.8-.2-.6 0-1.3.5-1.7z" fill="#1f8fd6"/>
          </svg>
          <span>+61 412 555 018</span>
        </div>
      </div>
      <h2 class="services-title">SERVICES PROVIDED</h2>
      <div class="service band">Executive Coaching</div>
      <div class="service">Leadership</div>
      <div class="service band-dark">NLP</div>
      <div class="service">Motivational Mapping</div>
      <div class="footer-band"></div>
    </div>
  </section>

  <section class="card card-front" aria-label="Card front">
    <div class="front-mark"></div>
    <div class="front-name">Orbell Consulting</div>
  </section>
</main>
</body>
</html>
```